Professional Website

We are looking for a new website for our Staffing Company. Attached is a document with all the details and pages needed along with some examples of others websites.

We want a professional Look and feel around the same color theme as the attached Vivid Vision.

We currently host our site on SiteKarn.io. If the winning designer can also add to SiteKarn, that is a plus.

```html
<!DOCTYPE html>
<html lang="en">
<head>
<meta charset="utf-8">
<title>Crewline Staffing</title>
<link href="https://fonts.googleapis.com/css2?family=Lato:wght@400;700;900&display=swap" rel="stylesheet">
<style>
:root{
  --brand:#2b2f92;
  --brand-deep:#232782;
  --ink:#2a2a2a;
  --dark:#232323;
  --white:#ffffff;
  --muted:#444;
}
*{box-sizing:border-box;margin:0;padding:0}
html,body{width:1200px;height:2207px;overflow:hidden;font-family:'Lato',sans-serif;color:var(--ink);background:var(--white)}
.page{position:relative;width:1200px;height:2207px}
.abs{position:absolute}
.logo-text{font-weight:900;color:var(--brand);font-size:44px;letter-spacing:-1px;line-height:1}
.logo-sub{font-weight:700;color:var(--brand);font-size:12px;letter-spacing:1px;margin-top:4px}

.topbar{left:373px;top:0;width:827px;height:51px;background:var(--dark);display:flex;align-items:center;gap:22px;padding-left:66px;color:#eee;font-size:14px}
.topbar .call b{font-weight:700}
.pill{border-radius:20px;padding:7px 14px;font-size:14px}
.pill-brand{background:var(--brand);color:#fff}
.pill-white{background:#fff;color:var(--brand)}
.sep{width:1px;height:24px;background:#555}
.nav{top:70px;left:665px;display:flex;gap:40px;font-size:17px;color:#222}
.nav .active{color:var(--brand);font-weight:700}

.hero{left:0;top:116px;width:1200px;height:617px;background:linear-gradient(120deg,#8a88c4 0%,#b7a79a 35%,#9a8a7a 60%,#6f5a4a 100%)}
.hero-title{left:0;top:350px;width:1200px;text-align:center;color:#fff;font-weight:900;font-size:48px;line-height:56px;text-shadow:0 2px 6px rgba(0,0,0,.35)}
.btn{display:flex;align-items:center;justify-content:center;border-radius:14px;font-weight:700;font-size:18px}
.btn-brand{background:var(--brand);color:#fff;border:2px solid #fff}
.btn-white{background:#fff;color:var(--brand)}
.arrow{stroke:#fff;stroke-width:2.5;fill:none}

.welcome-kicker{left:111px;top:798px;font-size:21px;font-weight:700;color:#222}
.welcome-title{left:111px;top:826px;font-size:39px;font-weight:900;color:var(--brand);display:flex;align-items:center;gap:14px}
.welcome-title span.rule{display:inline-block;width:62px;height:3px;background:var(--brand)}
.welcome-copy{left:111px;top:885px;width:540px;font-size:16.5px;line-height:30px;text-align:justify;color:#333}
.learn{left:111px;top:1123px;width:121px;height:58px}

.jobs{left:0;top:1249px;width:1200px;height:677px;background:linear-gradient(135deg,#262a8c,#2b2f94 50%,#24287f)}
.jobs-title{left:0;top:1304px;width:1200px;display:flex;justify-content:center;align-items:center;gap:18px;color:#fff;font-weight:900;font-size:39px}
.jobs-title .rule{width:52px;height:2px;background:#fff}
.job-photo{width:271px;height:271px;border-radius:50%;border:4px solid #fff}
.job{width:290px;text-align:center;color:#fff}
.job h3{font-size:17px;font-weight:700;margin-bottom:14px}
.job p{font-size:15px;line-height:30px}
.job a{display:inline-block;margin-top:2px;color:#fff;font-weight:700;font-size:17px;text-decoration:underline}

.foot-h{font-size:17px;font-weight:700;color:var(--brand)}
.foot-list{font-size:15px;line-height:30px;color:#333;list-style:none;margin-top:8px}
.social{display:flex;gap:8px}
.social span{width:40px;height:40px;border-radius:50%;border:1.5px solid #222}
.social span:last-child{border-color:var(--brand)}
.copy{font-size:13px;color:#333}
</style>
</head>
<body>
<div class="page">

  <header>
    <div class="abs" style="left:111px;top:34px">
      <div class="logo-text">Crewline</div>
      <div class="logo-sub">CLERICAL &amp; INDUSTRIAL</div>
    </div>
    <div class="abs topbar">
      <span class="call">&#9742; Call: <b>708-555-0147</b></span>
      <span class="sep"></span>
      <span class="pill pill-brand">Employee Login</span>
      <span class="sep"></span>
      <span class="pill pill-white">QuickPay Card Login</span>
      <span class="sep"></span>
      <span>Harbor Bank Login &#8594;</span>
    </div>
    <nav class="abs nav">
      <span class="active">Home</span><span>Jobs &#8964;</span><span>About</span><span>Contact</span>
    </nav>
  </header>

  <section>
    <div class="abs hero" role="img" aria-label="Photo of two professionals in an interview in a bright office lounge"></div>
    <h1 class="abs hero-title">RECRUITING AGENCY FOR TEMPORARY<br>AND DIRECT HIRE EMPLOYEES</h1>
    <div class="abs btn btn-brand" style="left:415px;top:495px;width:183px;height:62px">I’m looking for a Job</div>
    <div class="abs btn btn-white" style="left:620px;top:495px;width:167px;height:62px">I need Employees</div>
    <svg class="abs" style="left:30px;top:395px" width="60" height="40"><path class="arrow" d="M58 20H2M14 8L2 20l12 12"/></svg>
    <svg class="abs" style="left:1112px;top:395px" width="60" height="40"><path class="arrow" d="M2 20h56M46 8l12 12-12 12"/></svg>
  </section>

  <section>
    <div class="abs welcome-kicker">WELCOME TO</div>
    <h2 class="abs welcome-title">CREWLINE STAFFING <span class="rule"></span></h2>
    <p class="abs welcome-copy">Greatest part of our daily job is that we are constantly bringing people together. Our Clients come to us in search of the perfect candidate and the job hunters approach us when they are in need of a job or looking for their next exciting role. Being able to work with and connect the two is incredibly satisfying. Not to mention that in today's current job market, employers are fighting for the top talent. This makes our employees and partners grateful for the help in finding it!</p>
    <div class="abs btn" style="left:111px;top:1123px;width:121px;height:58px;background:var(--brand);color:#fff">Learn More</div>
    <svg class="abs" style="left:700px;top:780px" width="400" height="420" role="img" aria-label="Photo of a smiling man shaking hands">
      <defs><linearGradient id="tri" x1="0" y1="0" x2="1" y2="1"><stop offset="0" stop-color="#b9c8dc"/><stop offset=".6" stop-color="#8a8f9c"/><stop offset="1" stop-color="#c59a7c"/></linearGradient></defs>
      <path d="M340 10 Q387 -10 387 40 L387 360 Q387 410 340 390 L40 220 Q5 200 40 175 Z" fill="#fff" filter="drop-shadow(0 8px 14px rgba(0,0,0,.15))"/>
      <path d="M335 22 Q372 8 372 48 L372 352 Q372 392 335 378 L50 212 Q22 198 50 180 Z" fill="url(#tri)"/>
      <path d="M335 22 L50 180 Q22 198 50 212 L335 378" fill="none" stroke="var(--brand)" stroke-width="6"/>
    </svg>
  </section>

  <section>
    <div class="abs jobs"></div>
    <h2 class="abs jobs-title"><span class="rule"></span>JOBS PANEL<span class="rule"></span></h2>
    <svg class="abs" style="left:30px;top:1567px" width="60" height="40"><path class="arrow" d="M58 20H2M14 8L2 20l12 12"/></svg>
    <svg class="abs" style="left:1112px;top:1567px" width="60" height="40"><path class="arrow" d="M2 20h56M46 8l12 12-12 12"/></svg>

    <div class="abs job-photo" role="img" aria-label="Photo of a welder at work" style="left:132px;top:1412px;background:linear-gradient(160deg,#5a4a48,#3a3a6a 60%,#6a5a80)"></div>
    <div class="abs job-photo" role="img" aria-label="Photo of a material handler in a safety vest holding a clipboard" style="left:463px;top:1412px;background:linear-gradient(160deg,#5a5048,#9aa050 60%,#c6d640)"></div>
    <div class="abs job-photo" role="img" aria-label="Photo of two factory workers in blue overalls shaking hands" style="left:792px;top:1412px;background:linear-gradient(160deg,#4a4a4a,#2f5f9a 60%,#3a6aa8)"></div>

    <div class="abs job" style="left:123px;top:1724px"><h3>WELDERS</h3><p>We are hiring for, a reputed metal display company located in Hammond,</p><a>Apply Now</a></div>
    <div class="abs job" style="left:454px;top:1724px"><h3>MATERIAL HANDLERS</h3><p>You will be expected to work with a team and efficiently coordinate with them</p><a>Apply Now</a></div>
    <div class="abs job" style="left:783px;top:1724px"><h3>GENERAL LABOUR</h3><p>We are hiring for, a reputed metal display company located in Hammond,</p><a>Apply Now</a></div>
  </section>

  <footer>
    <div class="abs" style="left:111px;top:1993px">
      <div class="logo-text" style="font-size:46px">Crewline</div>
      <div class="logo-sub">CLERICAL &amp; INDUSTRIAL</div>
    </div>
    <div class="abs social" style="left:111px;top:2087px"><span></span><span></span><span></span><span></span></div>
    <div class="abs copy" style="left:110px;top:2142px">2022 Crewline Staffing. All Rights Reserved.</div>

    <div class="abs" style="left:473px;top:1990px"><div class="foot-h">QUICK LINK</div>
      <ul class="foot-list"><li>Home</li><li>About</li><li>Jobs</li><li>Contact</li></ul></div>
    <div class="abs" style="left:670px;top:1990px"><div class="foot-h">AREAS WE SERVICE</div>
      <ul class="foot-list"><li>Blue Island</li><li>Alsip</li><li>Romeoville</li></ul></div>
    <div class="abs" style="left:927px;top:1990px"><div class="foot-h">CONTACT US</div>
      <ul class="foot-list">
        <li><span style="color:var(--brand)">&#9679;</span> Crewline Staffing</li>
        <li style="padding-left:20px">Address Comes Here</li>
        <li style="margin-top:8px;color:var(--brand)">&#9742; 708-555-0147</li>
        <li style="margin-top:8px"><span style="color:var(--brand)">&#9993;</span> info@crewlinestaffing.com</li>
      </ul></div>
  </footer>

</div>
</body>
</html>
```